Customizable Gift Note Card Design

I need a gift note card designed for my Healthy Snacks Care Package company. I need to be able to customize each card with the customer's gift message to the recipient and print to a standard printer.

The card should be single-sided 5 x 7, include our logo, keep colors and graphics simple since they will be printed for each individual order on a standard printer. I would like the following quote to be included in a small and subtle way: "Food is symbolic of love when words are inadequate." —Bertram K. Osslund. Our website thebrightpantrybites.example should also be included.

I have included pictures of our product packaging for reference.

Target Market(s)

Gift recipients: Students, people recovering from illness, housewarming, thank you gifts...etc.

Industry/Entity Type

It Company

Colors

Designer to choose colors to be used in the design.

Requirements
Must have
• We are looking for a simple, cute and elegant gift card that reflects our branding. Must be customizable and printable on a standard printer.
• Must be single-sided 5x7.

```html
<!DOCTYPE html>
<html lang="en">
<head>
<meta charset="utf-8">
<title>The Bright Pantry – Gift Note Card</title>
<link rel="stylesheet" href="https://fonts.googleapis.com/css2?family=Open+Sans:wght@400;700;800&display=swap">
<style>
  :root {
    --paper: #ffffff;
    --ink: #1a1a1a;
    --quote-outline: #dadada;
    --byline: #c8c8c8;
    --mascot-tone: #ececec;
    --mascot-tone-deep: #dedede;
  }
  * { box-sizing: border-box; margin: 0; padding: 0; }
  html, body {
    width: 1200px; height: 855px; overflow: hidden;
    background: var(--paper);
  }
  .gift-card {
    position: relative;
    width: 1200px; height: 855px;
    background: var(--paper);
    font-family: "Open Sans", Arial, sans-serif;
    color: var(--ink);
  }
  .greeting {
    position: absolute; left: 111px; top: 205px;
    font-size: 22px; line-height: 30px;
  }
  .message {
    position: absolute; left: 111px; top: 300px;
    font-size: 22px; line-height: 31px;
    white-space: nowrap;
  }
  .quote {
    position: absolute; left: 40px; top: 428px;
    font-size: 50px; font-weight: 800; line-height: 62px;
    white-space: nowrap;
    color: var(--paper);
    -webkit-text-stroke: 1.5px var(--quote-outline);
  }
  .quote-author {
    font-size: 20px; font-weight: 700;
    color: var(--byline);
    -webkit-text-stroke: 0;
    margin-left: 12px;
    vertical-align: 6px;
  }
  .sign-off {
    position: absolute; left: 111px; top: 602px;
    font-size: 22px; line-height: 37px;
  }
  .brand-block {
    position: absolute; left: 96px; top: 736px;
    display: flex; align-items: center; gap: 12px;
  }
  .brand-dot {
    width: 30px; height: 30px; border-radius: 50%;
    background: var(--ink);
  }
  .brand-text { display: flex; flex-direction: column; }
  .brand-name {
    font-size: 20px; font-weight: 700; color: var(--ink); line-height: 24px;
  }
  .brand-site {
    font-size: 13px; color: var(--ink); line-height: 18px;
  }
  .mascot-area {
    position: absolute; left: 950px; top: 76px;
    width: 250px; height: 710px;
    border-radius: 125px 0 0 125px;
    background: linear-gradient(180deg, var(--mascot-tone-deep), var(--mascot-tone) 45%, var(--mascot-tone-deep));
  }
</style>
</head>
<body>
  <main class="gift-card">
    <p class="greeting">Dear Client</p>
    <p class="message">This parcel has been sent to you by someone who thinks your<br>pretty awesome. We hope you do enjoy the surprise and the goodies<br>which you received.</p>

    <p class="quote">‘Food is symbolic of love when<br>words are inadequate’<span class="quote-author">by Bertram K. Osslund</span></p>

    <p class="sign-off">With our best compliments<br>Name / Signature</p>

    <div class="brand-block">
      <span class="brand-dot"></span>
      <div class="brand-text">
        <span class="brand-name">the Bright Pantry</span>
        <span class="brand-site">thebrightpantrybites.example</span>
      </div>
    </div>

    <div class="mascot-area" role="img" aria-label="Brand mascot decoration: gentleman with hat, red glasses, moustache and bow tie"></div>
  </main>
</body>
</html>
```